automotive repair and collision repair shop card

our company is called K.R Motor service we are a automotive repair company
we also do government inspections. the company information is on the cards. I would like you to use my new logo and create a new card and use the information from my old card. Good Luck!!

Industry/Entity Type

Car Repair

Contact Information for Business Card

Address: #417-15862 91 Ave, Surrey, BC V5T 8K4
Phone:(604) 555-0187
fax 604 555 0142
website www.krmotor.example

Font styles to use
Serif
Sans Serif

Requirements
Must have
• all the information
Should not have
• the owner and there name

```html
<!DOCTYPE html>
<html lang="en">
<head>
<meta charset="utf-8">
<title>K.R Motor service – Business Card</title>
<link href="https://fonts.googleapis.com/css2?family=Saira:wght@400;600;700&display=swap" rel="stylesheet">
<style>
  :root {
    --canvas: #e9e7e3;
    --ink: #0b0b0b;
    --text-light: #f2f2f2;
    --art-dark: #2a2a2a;
    --art-mid: #8a8a8a;
    --art-light: #e6e6e6;
  }
  * { margin: 0; padding: 0; box-sizing: border-box; }
  html, body { width: 1200px; height: 780px; overflow: hidden; }
  body {
    background: var(--canvas);
    font-family: "Saira", "Arial", sans-serif;
    position: relative;
  }
  .card {
    position: absolute;
    top: 232px;
    width: 540px;
    height: 316px;
    border-radius: 22px;
    overflow: hidden;
    background: var(--ink);
    box-shadow: 0 10px 28px rgba(0,0,0,.25);
  }
  .card--front { left: 40px; }
  .card--back { left: 620px; }

  /* front */
  .front-top {
    position: absolute; inset: 0 0 auto 0; height: 190px;
  }
  .front-top svg { display: block; width: 100%; height: 100%; }
  .logo-art {
    position: absolute; left: 130px; top: 26px; width: 170px; height: 92px;
    border-radius: 46px;
    background: radial-gradient(ellipse at center, var(--art-mid) 0%, var(--art-dark) 70%, transparent 72%);
  }
  .brand {
    position: absolute; left: 310px; top: 44px;
    color: var(--art-dark);
  }
  .brand-name { font-size: 24px; font-weight: 600; line-height: 1; white-space: nowrap; }
  .brand-tag { font-size: 11px; font-weight: 400; margin-top: 6px; letter-spacing: .5px; }

  .contact {
    position: absolute; left: 60px; top: 192px;
    color: var(--text-light);
    font-size: 13.5px; line-height: 1.3;
  }
  .contact-line { display: flex; align-items: center; gap: 7px; }
  .contact-icon {
    width: 14px; height: 14px; border-radius: 3px; background: var(--text-light);
    display: inline-flex; align-items: center; justify-content: center; flex: none;
  }
  .contact-icon svg { width: 10px; height: 10px; }

  /* back */
  .back-art {
    position: absolute; left: 40px; top: 26px; width: 460px; height: 150px;
    border-radius: 70px 110px 40px 40px;
    background: linear-gradient(180deg, var(--art-light) 0%, #bdbdbd 100%);
  }
  .services {
    position: absolute; left: 28px; right: 24px; top: 196px; color: var(--text-light);
  }
  .services-title { font-size: 17px; font-weight: 700; margin-bottom: 6px; }
  .services-list { font-size: 14px; line-height: 1.45; }
</style>
</head>
<body>

<section class="card card--front" aria-label="Card front">
  <div class="front-top">
    <svg viewBox="0 0 540 190" preserveAspectRatio="none" aria-hidden="true">
      <defs>
        <linearGradient id="silver" x1="0" y1="0" x2="0" y2="1">
          <stop offset="0" stop-color="#ffffff"/>
          <stop offset="1" stop-color="#d4d4d4"/>
        </linearGradient>
      </defs>
      <path d="M0 0 H540 V70 Q290 230 0 138 Z" fill="url(#silver)"/>
      <path d="M0 138 Q290 230 540 70" fill="none" stroke="#ffffff" stroke-width="3"/>
    </svg>
    <div class="logo-art" role="img" aria-label="Stylised sports car illustration in grey tones"></div>
    <div class="brand">
      <div class="brand-name">K.R Motor service</div>
      <div class="brand-tag">One Stop Repair Shop</div>
    </div>
  </div>

  <div class="contact">
    <div class="contact-line">#417-15862 91 Ave</div>
    <div class="contact-line">Surrey, BC V5T 8K4</div>
    <div class="contact-line">
      <span class="contact-icon"><svg viewBox="0 0 10 10"><path d="M2 1h2l1 2-1 1q1 2 2 2l1-1 2 1v2q-4 1-7-3T2 1z" fill="#0b0b0b"/></svg></span>
      (604) 555-0187</div>
    <div class="contact-line">
      <span class="contact-icon"><svg viewBox="0 0 10 10"><rect x="2" y="1" width="6" height="3" fill="#0b0b0b"/><rect x="1" y="4" width="8" height="4" fill="#0b0b0b"/></svg></span>
      604 555 0142</div>
    <div class="contact-line">
      <span class="contact-icon"><svg viewBox="0 0 10 10"><rect x="1" y="2" width="8" height="6" fill="none" stroke="#0b0b0b"/><path d="M1 2l4 3 4-3" fill="none" stroke="#0b0b0b"/></svg></span>
      info@krmotor.example</div>
    <div class="contact-line">
      <span class="contact-icon"><svg viewBox="0 0 10 10"><circle cx="5" cy="5" r="4" fill="none" stroke="#0b0b0b"/><path d="M1 5h8M5 1q-2 4 0 8M5 1q2 4 0 8" fill="none" stroke="#0b0b0b" stroke-width=".8"/></svg></span>
      www.krmotor.example</div>
  </div>
</section>

<section class="card card--back" aria-label="Card back">
  <div class="back-art" role="img" aria-label="Large white line-art sports car in side view"></div>
  <div class="services">
    <div class="services-title">Call us for:</div>
    <div class="services-list">
      Oil Change / Scheduled maintenance / Body Work / Paint<br>
      Glass Replacement / Insurance Claims / Inspections / Engine repair
    </div>
  </div>
</section>

</body>
</html>
```